Need a Car Magnet designed

I need a car magnet designed.

The dimensions have to be 9" width by 2.6" height.

It needs to say PLOVA TRIP and include the attached logo

```html
<!DOCTYPE html>
<html lang="en">
<head>
<meta charset="utf-8">
<title>PLOVA TRIP car magnet</title>
<link rel="stylesheet" href="https://fonts.googleapis.com/css2?family=Cinzel:wght@700;900&display=swap">
<style>
  :root {
    --backdrop: #5a5a5a;
    --ball-light: #f4f4f4;
    --ball-shade: #d9d9d9;
    --tour-blue: #1d428a;
    --badge-red: #d22f1c;
  }
  html, body {
    margin: 0;
    padding: 0;
    width: 1200px;
    height: 825px;
    overflow: hidden;
    background: var(--backdrop);
  }
  .canvas {
    position: relative;
    width: 1200px;
    height: 825px;
  }
  .magnet {
    position: absolute;
    left: 118px;
    top: 274px;
    width: 964px;
    height: 276px;
  }
  .magnet-texture {
    fill: url(#ballSurface);
  }
  .brand-mark {
    fill: var(--badge-red);
  }
  .brand-name {
    font-family: "Cinzel", serif;
    font-weight: 700;
    font-size: 30px;
    fill: var(--tour-blue);
  }
  .headline {
    font-family: "Cinzel", serif;
    font-weight: 900;
    fill: var(--tour-blue);
  }
</style>
</head>
<body>
<main class="canvas">
  <svg class="magnet" viewBox="0 0 964 276" xmlns="http://www.w3.org/2000/svg">
    <defs>
      <linearGradient id="ballSurface" x1="0" y1="0" x2="1" y2="1">
        <stop offset="0" stop-color="var(--ball-shade)"/>
        <stop offset="0.5" stop-color="var(--ball-light)"/>
        <stop offset="1" stop-color="var(--ball-shade)"/>
      </linearGradient>
    </defs>

    <rect class="magnet-texture" x="0" y="0" width="964" height="276"
          role="img" aria-label="Golf ball dimple surface background"/>

    <g class="brand-lockup">
      <circle class="brand-mark" cx="62" cy="122" r="26"/>
      <text class="brand-name" x="100" y="133">PLOVA TRIP</text>
    </g>

    <g class="headline-group">
      <text class="headline" x="582" y="86" font-size="150" text-anchor="middle"
            dominant-baseline="middle" textLength="560" lengthAdjust="spacingAndGlyphs"
            transform="rotate(-9 582 86)">PLOVA</text>
      <text class="headline" x="730" y="194" font-size="150" text-anchor="middle"
            dominant-baseline="middle" textLength="430" lengthAdjust="spacingAndGlyphs"
            transform="rotate(-9 730 194)">TRIP</text>
    </g>
  </svg>
</main>
</body>
</html>
```